Cousin Wexley's Puttro Project

Create a design with the words, "Cousin Wexley's Putt-row Kit". This design will be featured on the product itself. The product will entail a kit of items to help auto body and painters make repairs. The kit itself will be at least one foot long/wide when packaged.

The design should be more than just the logo....it will need to be on the cover of the product which is approx 8" by 8".

Target Market(s)

Anyone who repairs fiberglass, hard surface products for a living...auto, boats, decks, drywall, etc. Largely blue collar DIY men.

Requirements
Must have
• Some of the design must have a see-through/clear section so that customers can see what is in the package.
Nice to have
• In an ideal world, the design could be expanded or shrunk but should be about 1" high.
Should not have
• No cartoon characters.

```html
<!DOCTYPE html>
<html lang="en">
<head>
<meta charset="utf-8">
<title>Cousin Wexley's Putt-row Kit</title>
<link rel="stylesheet" href="https://fonts.googleapis.com/css2?family=Roboto+Condensed:wght@400;700;900&family=Montserrat:wght@400;600;700&display=swap">
<style>
  :root {
    --stage: #808a9a;
    --pack-blue: #28acd8;
    --pack-black: #141416;
    --pack-white: #e9eef1;
    --ring-blue: #2fa9d6;
    --text-dark: #161616;
    --text-light: #ffffff;
    --fill-grey: #c9ccd3;
  }
  * { margin: 0; padding: 0; box-sizing: border-box; }
  html, body { width: 1200px; height: 1000px; overflow: hidden; }
  body { background: var(--stage); position: relative; font-family: "Montserrat", sans-serif; }

  .package {
    position: absolute; left: 400px; top: 225px; width: 400px; height: 540px;
    background: var(--pack-blue); overflow: hidden;
  }
  .package-shapes { position: absolute; inset: 0; }

  .brand-row {
    position: absolute; left: 40px; top: 148px; display: flex; align-items: center; gap: 10px;
  }
  .brand-square { width: 62px; height: 30px; background: var(--pack-white); }
  .brand-name {
    font-family: "Roboto Condensed", sans-serif; font-weight: 900; font-size: 38px;
    color: var(--text-dark); line-height: 1; letter-spacing: 0.5px; white-space: nowrap;
  }

  .kit-band {
    position: absolute; left: 0; top: 195px; width: 400px; height: 30px;
    background: var(--pack-black); display: flex; align-items: center; padding-left: 90px;
  }
  .kit-title { font-weight: 700; font-size: 19px; color: var(--text-light); }

  .kit-blurb {
    position: absolute; left: 90px; top: 234px; width: 300px;
    font-size: 7px; line-height: 1.45; color: #1d4c60;
  }

  .feature-pill {
    position: absolute; left: 200px; top: 282px; width: 215px; height: 18px;
    background: var(--pack-black); border-radius: 9px;
    display: flex; align-items: center; justify-content: space-around; padding-right: 20px;
    font-family: "Roboto Condensed", sans-serif; font-size: 8px; color: var(--text-light);
  }

  .contents-window {
    position: absolute; left: 302px; top: 395px; width: 85px; height: 105px;
    border-radius: 10px; border: 3px solid #1f2a33;
    background: radial-gradient(circle at 40% 40%, #f0f1f4, var(--fill-grey) 60%, #9fa4ae);
  }

  .net-weight {
    position: absolute; left: 8px; top: 512px; font-size: 10px; color: var(--text-light);
  }
</style>
</head>
<body>
  <div class="package">
    <svg class="package-shapes" width="400" height="540" viewBox="0 0 400 540">
      <polygon points="0,0 170,0 45,150 0,150" fill="var(--pack-black)"/>
      <polygon points="178,0 205,0 85,128 60,128" fill="var(--pack-white)"/>
      <polygon points="0,330 110,330 260,540 0,540" fill="var(--pack-black)"/>
      <polygon points="110,330 178,330 345,540 260,540" fill="var(--pack-white)"/>

      <g class="use-icon boat">
        <circle cx="143" cy="372" r="22" fill="var(--pack-black)" stroke="var(--ring-blue)" stroke-width="4"/>
        <polygon points="143,357 143,378 131,378" fill="#fff"/>
        <polygon points="146,360 146,378 156,378" fill="#fff"/>
        <path d="M129 381 h28 l-4 5 h-20 z" fill="#fff"/>
      </g>
      <g class="use-icon wall">
        <circle cx="205" cy="447" r="22" fill="var(--pack-black)" stroke="var(--ring-blue)" stroke-width="4"/>
        <g stroke="#fff" stroke-width="1.5" fill="none">
          <rect x="193" y="436" width="24" height="22"/>
          <line x1="193" y1="443" x2="217" y2="443"/>
          <line x1="193" y1="451" x2="217" y2="451"/>
          <line x1="205" y1="436" x2="205" y2="443"/>
          <line x1="199" y1="443" x2="199" y2="451"/>
          <line x1="211" y1="443" x2="211" y2="451"/>
          <line x1="205" y1="451" x2="205" y2="458"/>
        </g>
      </g>
      <g class="use-icon car">
        <circle cx="268" cy="510" r="22" fill="var(--pack-black)" stroke="var(--ring-blue)" stroke-width="4"/>
        <path d="M252 514 v-5 l6 -2 l5 -5 h11 l6 5 l4 2 v5 z" fill="none" stroke="#fff" stroke-width="1.5"/>
        <circle cx="259" cy="515" r="2.5" fill="#fff"/>
        <circle cx="277" cy="515" r="2.5" fill="#fff"/>
      </g>
    </svg>

    <div class="brand-row">
      <span class="brand-square"></span>
      <span class="brand-name">COUSIN WEXLEY'S</span>
    </div>

    <div class="kit-band"><span class="kit-title">Putt-row Kit</span></div>

    <p class="kit-blurb">Everything you need to fill dents, cracks and holes in fiberglass, metal and wood. Mix, spread, sand and paint for a smooth, lasting repair.</p>

    <div class="feature-pill">
      <span>• Paintable</span><span>• Permanent</span><span>• Non-Shrinking</span>
    </div>

    <div class="contents-window" role="img" aria-label="Clear window showing the grey filler powder inside the pack"></div>

    <span class="net-weight">Net Wt. 7.56 lb</span>
  </div>
</body>
</html>
```